VORdyne stands for Valve & Output Regulation dynamics and specialises in process automation

We are a New company called VORdyne (Valve & Output Regulation dynamics) a Brisbane based company speciallising in Process Automation for the oil and Gas industry in Australia. We work on projects for DCS, RTU and PLC automation this involves programming and commissioning. We initially need a Website that customers can see about the company and make enquiries. We currently have Royal Blue and grey as our colours on our email signatures but are open for suggestions. Keywords i would suggest yo to look at for insperation are CSG ( coalseam gas) DCS (Distributed control system) RTU (remote terminal unit) and PLC (programmable logic controller).

Target Market(s)

Large CSG companies in Australia, Tellory, Brenmark, HJV, Fenwy

Industry/Entity Type

Industry

```html
<!DOCTYPE html>
<html lang="en">
<head>
<meta charset="utf-8">
<title>VORdyne – Valve &amp; Output Regulation dynamics</title>
<link href="https://fonts.googleapis.com/css2?family=PT+Sans:wght@400;700&display=swap" rel="stylesheet">
<style>
  :root{
    --royal:#0a0aff;
    --ink:#333;
    --muted:#666;
    --line:#d9d9d9;
    --footer:#2a2a2a;
    --white:#fff;
  }
  html,body{margin:0;padding:0;width:984px;height:1200px;overflow:hidden;background:var(--white);}
  body{font-family:"PT Sans",Arial,sans-serif;color:var(--ink);}
  .page{position:relative;width:1000px;height:1220px;transform:scale(.984);transform-origin:0 0;}
  .abs{position:absolute;}
  .brand{left:72px;top:38px;margin:0;font-size:25px;font-weight:700;color:var(--royal);letter-spacing:.2px;}
  .tagline{left:72px;top:72px;font-size:13px;color:#555;}
  .search{left:738px;top:56px;width:187px;height:27px;border:1px solid #c9c9c9;border-radius:3px;box-sizing:border-box;
    font-size:11px;font-style:italic;color:#999;padding:6px 8px;}
  .search svg{position:absolute;right:8px;top:7px;}
  .nav{left:0;top:115px;width:1000px;height:38px;background:var(--royal);}
  .nav ul{list-style:none;margin:0;padding:0;}
  .nav li{position:absolute;top:11px;color:var(--white);font-size:14px;text-transform:uppercase;}
  .hero{left:72px;top:167px;width:856px;height:383px;
    background:linear-gradient(180deg,#2d3e55 0%,#5f7896 40%,#8ea4bd 70%,#c9d5e2 100%);}
  .hero-shadow{left:150px;top:550px;width:700px;height:30px;
    background:radial-gradient(ellipse at top,rgba(0,0,0,.18),rgba(0,0,0,0) 70%);}
  .caption{left:540px;top:350px;width:328px;height:98px;background:rgba(60,60,60,.72);color:var(--white);box-sizing:border-box;padding:12px 14px;}
  .caption h2{margin:0 0 6px;font-size:17px;font-weight:700;}
  .caption p{margin:0;font-size:13px;line-height:21px;}
  .slide-btn{top:515px;width:25px;height:25px;background:rgba(90,90,90,.8);}
  .service{width:192px;}
  .service h3{margin:0;font-size:14px;font-weight:400;color:var(--royal);}
  .thumb{margin-top:7px;width:190px;height:128px;border:1px solid var(--line);box-sizing:border-box;padding:3px;}
  .thumb div{width:100%;height:100%;}
  .service p{margin:13px 0 0;font-size:11px;line-height:18px;color:var(--muted);}
  .more{display:block;margin-top:12px;font-size:11px;color:#444;}
  .more span{margin-left:12px;}
  .section-title{margin:0;font-size:17px;font-weight:400;color:var(--royal);}
  .welcome-img{left:70px;top:900px;width:247px;height:188px;border:1px solid var(--line);box-sizing:border-box;padding:3px;}
  .welcome-img div{width:100%;height:100%;background:linear-gradient(135deg,#2c3440,#56606d 55%,#c9ccd1);}
  .welcome-text{left:340px;top:898px;width:305px;}
  .lead{margin:0 0 10px;font-size:13px;line-height:22px;color:#444;}
  .body{margin:0 0 4px;font-size:11px;line-height:19px;color:var(--muted);}
  .news-item{left:689px;width:240px;height:52px;}
  .news-thumb{position:absolute;left:0;top:0;width:58px;height:50px;border:1px solid var(--line);box-sizing:border-box;padding:3px;}
  .news-thumb div{width:100%;height:100%;}
  .news-text{position:absolute;left:71px;top:-6px;width:172px;font-size:11px;line-height:18px;color:#555;}
  .news-text b{color:#444;}
  .footer{left:0;top:1125px;width:1000px;height:95px;background:var(--footer);color:var(--white);}
  .footer-links{left:71px;top:21px;font-size:12px;}
  .footer-links span{color:#aaa;margin:0 3px;}
  .copy{left:72px;top:54px;font-size:11px;}
  .social{top:26px;width:27px;height:27px;border-radius:4px;}
  .newsletter{left:675px;top:32px;font-size:13px;}
  .news-input{left:752px;top:26px;width:169px;height:29px;background:var(--white);border-radius:2px;}
  .news-input svg{position:absolute;right:6px;top:9px;}
</style>
</head>
<body>
<div class="page">
  <header>
    <h1 class="abs brand">VORdyne</h1>
    <div class="abs tagline">Valve &amp; Output Regulation dynamics</div>
    <div class="abs search">Search..
      <svg width="12" height="12" viewBox="0 0 12 12"><circle cx="5" cy="5" r="3.8" fill="none" stroke="#999" stroke-width="1.6"/><line x1="8" y1="8" x2="11" y2="11" stroke="#999" stroke-width="1.8"/></svg>
    </div>
  </header>

  <nav class="abs nav">
    <ul>
      <li style="left:87px">Home</li>
      <li style="left:173px">About us</li>
      <li style="left:284px">Services</li>
      <li style="left:388px">Products</li>
      <li style="left:503px">Blog</li>
      <li style="left:585px">Latest News</li>
      <li style="left:716px">Testimonials</li>
      <li style="left:852px">Contact</li>
    </ul>
  </nav>

  <section>
    <div class="abs hero" role="img" aria-label="Photo of an engineer at a control room desk facing wall-mounted process monitors"></div>
    <div class="abs hero-shadow"></div>
    <div class="abs caption">
      <h2>Amet dolor sit tation ullamcorper</h2>
      <p>Donec id ante magna. Nullam sollicitudin, ipsum vel hendrerit aliquam, nisi sapien pellentesque odio.</p>
    </div>
    <div class="abs slide-btn" style="left:93px"><svg width="25" height="25"><polyline points="15,8 10,12.5 15,17" fill="none" stroke="#fff" stroke-width="1.5"/></svg></div>
    <div class="abs slide-btn" style="left:122px"><svg width="25" height="25"><polyline points="10,8 15,12.5 10,17" fill="none" stroke="#fff" stroke-width="1.5"/></svg></div>
  </section>

  <section>
    <div class="abs service" style="left:74px;top:593px">
      <h3>Coalseam gas</h3>
      <div class="thumb"><div role="img" aria-label="Photo of two field workers in hard hats at a gas wellhead" style="background:linear-gradient(180deg,#4a6fa8,#2c3c5c 60%,#a08a5a)"></div></div>
      <p>Lorem ipsum dolor sit amet, consectet uer adipiscing elit. Mauris vel tortor vit ae nibh condimentum auctor.</p>
      <span class="more">READ MORE<span>»</span></span>
    </div>
    <div class="abs service" style="left:295px;top:593px">
      <h3>Distributed control system</h3>
      <div class="thumb"><div role="img" aria-label="Photo of a control system monitor on an operator desk" style="background:linear-gradient(135deg,#3a2a10,#1e1e1e 50%,#4aa7b8)"></div></div>
      <p>Lorem ipsum dolor sit amet, consectet uer adipiscing elit. Mauris vel tortor vit ae nibh condimentum auctor.</p>
      <span class="more">READ MORE<span>»</span></span>
    </div>
    <div class="abs service" style="left:517px;top:593px">
      <h3>Remote Terminal Unit</h3>
      <div class="thumb"><div role="img" aria-label="Photo of a remote terminal unit panel with switches and connectors" style="background:linear-gradient(135deg,#6b6e6a,#9a9c98 50%,#4a5a52)"></div></div>
      <p>Lorem ipsum dolor sit amet, consectet uer adipiscing elit. Mauris vel tortor vit ae nibh condimentum auctor.</p>
      <span class="more">READ MORE<span>»</span></span>
    </div>
    <div class="abs service" style="left:736px;top:593px">
      <h3>Programmable Logic Controller</h3>
      <div class="thumb"><div role="img" aria-label="Photo of a rack of programmable logic controller modules" style="background:linear-gradient(180deg,#4a5560,#7d8893 55%,#3b5fbf)"></div></div>
      <p>Lorem ipsum dolor sit amet, consectet uer adipiscing elit. Mauris vel tortor vit ae nibh condimentum auctor.</p>
      <span class="more">READ MORE<span>»</span></span>
    </div>
  </section>

  <section>
    <h2 class="abs section-title" style="left:71px;top:869px">Welcome to our website</h2>
    <div class="abs welcome-img"><div role="img" aria-label="Photo of an operator seated at a bank of control room screens"></div></div>
    <div class="abs welcome-text">
      <p class="lead">Duis autem vel eum iriure dolor in hendrerit in vulpi utate velit esse molestie consequat</p>
      <p class="body">Incididunt ut labore et dolore magna aliqua. Ut enim ad mini m veniam, quis nostrud exercitation ullamcolaboris nisi ut ali quip ex ea commodo consequat. Duis tefd&nbsp; aute iruredolor in reprehenderit in&nbsp; voluptate velit esse cillum.</p>
      <p class="body">Dolore magna aliqua. Ut enim ad minim veniam, quisnostrud exercitation ullamco laboris nisi ut aliquip. Ut enim ad minim veniam, quis nostrud exercitation ullamco laboris .</p>
    </div>
  </section>

  <aside>
    <h2 class="abs section-title" style="left:691px;top:869px">Latest News</h2>
    <div class="abs news-item" style="top:899px">
      <div class="news-thumb"><div role="img" aria-label="Portrait photo" style="background:linear-gradient(135deg,#c9a56a,#8d6a45)"></div></div>
      <div class="news-text"><b>During November 2013</b><br>our Principal Petrophysicist, quis strud exercitation ullamco labors.</div>
    </div>
    <div class="abs news-item" style="top:969px">
      <div class="news-thumb"><div role="img" aria-label="Portrait photo" style="background:linear-gradient(135deg,#9aa79a,#7a5a48)"></div></div>
      <div class="news-text"><b>During November 2013</b><br>At vero eos et accusamus et iusto dio dignissimos ducimus qui.</div>
    </div>
    <div class="abs news-item" style="top:1041px">
      <div class="news-thumb"><div role="img" aria-label="Portrait photo" style="background:linear-gradient(135deg,#e8e8ec,#8a8f99)"></div></div>
      <div class="news-text"><b>During November 2013</b><br>Deleniti atque corrupti quos does et quas molestias excepturi sint.</div>
    </div>
  </aside>

  <footer class="abs footer">
    <div class="abs footer-links">Home<span>¦</span>About us<span>¦</span>Services<span>¦</span>Products<span>¦</span>Blog<span>¦</span>Latest News<span>¦</span>Testimonials<span>¦</span>Contact</div>
    <div class="abs copy">Copyrights 2013. All Rights Reserved.</div>
    <div class="abs social" style="left:540px;background:#e8771f"></div>
    <div class="abs social" style="left:575px;background:#3b5998"></div>
    <div class="abs social" style="left:611px;background:#2aa3e0"></div>
    <div class="abs newsletter">Newsletter</div>
    <div class="abs news-input"><svg width="14" height="12"><polyline points="2,1 6,6 2,11" fill="none" stroke="#999" stroke-width="1.5"/><polyline points="7,1 11,6 7,11" fill="none" stroke="#999" stroke-width="1.5"/></svg></div>
  </footer>
</div>
</body>
</html>
```